Broschüre für Sprachschule für die Vorstellung der Leistungen
Zielgruppe
Es geht um eine Broschüre einer Sprachschule für die Vorstellung der Leistungen:
Sprachkurse: A1, A2, B1. B2, C1, Fachsprache Ärzte, Fachspräche Pflegepersonal, Fachsprache Ingenieure
Seminare: Businessplan für Migranten, Unternehmensführung für Migranten, Ausbildung zur Pflegefachkraft, Existenzgründung für Migranten
Aufgabenstellung
Es handelt sich um ein Sprachschule/Bildungszentrum. Farben: Royal Blau, Gold

```html
<!DOCTYPE html>
<html lang="de">
<head>
<meta charset="utf-8">
<title>Sprachschule Broschüre</title>
<link href="https://fonts.googleapis.com/css2?family=Source+Sans+3:wght@400;700&display=swap" rel="stylesheet">
<style>
:root{
  --royal:#143f8f;
  --gold:#fcc72c;
  --ink:#1a1a1a;
  --paper:#ffffff;
  --rule:#d8d8d8;
}
*{margin:0;padding:0;box-sizing:border-box}
html,body{width:848px;height:1200px;overflow:hidden;background:var(--paper)}
body{font-family:"Source Sans 3",sans-serif;color:var(--ink)}
.canvas{position:relative;width:848px;height:1200px;overflow:hidden}
.page{position:absolute;overflow:hidden;background:var(--paper)}
.page-cover{left:0;top:0;width:423px;height:599px}
.page-route{left:425px;top:0;width:423px;height:599px;border-left:1px solid var(--rule)}
.page-philosophy{left:0;top:601px;width:424px;height:599px}
.page-services{left:424px;top:601px;width:424px;height:599px}
.abs{position:absolute}
.heading{position:absolute;color:var(--royal);font-weight:700;white-space:nowrap;line-height:1}
.body-text{position:absolute;font-size:10px;line-height:12px;white-space:nowrap;color:var(--ink)}
.body-text div{display:block}
.small-blue{position:absolute;font-size:8px;line-height:9.7px;color:var(--royal);white-space:nowrap}
.brand-mark{position:absolute;display:flex;align-items:center;gap:7px;color:var(--royal);font-weight:700;white-space:nowrap}
.brand-mark .brand-dot{display:block;border-radius:50%;background:var(--gold)}
.footer-band{position:absolute;left:0;bottom:0;width:423px;height:49px;background:var(--gold);color:#fff;font-weight:700;font-size:12px;padding-left:10px;display:flex;align-items:center;white-space:nowrap}
.cover-title{left:130px;top:416px;font-size:42px;line-height:51px}
.offer-list{position:absolute;font-size:10px;line-height:12px;color:var(--ink)}
.offer-item{position:absolute;white-space:nowrap}
.offer-item .dot{position:absolute;left:-14px;top:3px;width:7px;height:7px;border-radius:50%}
.dot-gold{background:var(--gold)}
.dot-royal{background:var(--royal)}
.page-number{position:absolute;left:20px;top:569px;color:#fff;font-size:9px;font-weight:700}
</style>
</head>
<body>
<div class="canvas">

  <section class="page page-cover">
    <svg class="abs" style="left:0;top:0" width="423" height="400" viewBox="0 0 423 400">
      <defs>
        <linearGradient id="coverPhotoTone" x1="0" y1="0" x2="1" y2="1">
          <stop offset="0" stop-color="#8a7a66"/>
          <stop offset="0.45" stop-color="#c9a88e"/>
          <stop offset="1" stop-color="#6f6a74"/>
        </linearGradient>
      </defs>
      <path d="M0 290 Q205 485 423 292 L423 0 L0 0 Z" fill="var(--royal)"/>
      <path d="M0 0 L423 0 L423 288 Q190 440 0 322 Z" fill="url(#coverPhotoTone)" role="img" aria-label="Foto: Pflegekraft legt einer älteren Dame eine karierte Decke um"/>
    </svg>

    <div class="brand-mark" style="left:24px;top:450px;font-size:16px">
      <span class="brand-dot" style="width:16px;height:16px"></span>
      <span class="brand-name">Ihr Logo</span>
    </div>

    <h1 class="heading cover-title">Sprachschule<br>Lorem ipsum</h1>

    <div class="footer-band">Logo, ggf Förderhinweise, Adresse, Kontaktdaten, besondere Hinweise etc</div>
  </section>

  <section class="page page-route">
    <h2 class="heading" style="left:123px;top:34px;font-size:24px">Ihr Weg zu uns</h2>
    <h2 class="heading" style="left:160px;top:63px;font-size:24px">Your way to us</h2>

    <div class="brand-mark" style="left:37px;top:132px;font-size:13px">
      <span class="brand-dot" style="width:12px;height:12px"></span>
      <span class="brand-name">Ihr Logo</span>
    </div>

    <div class="small-blue" style="left:37px;top:182px">Mitarbeiter<br>Adresse<br>Kontaktdaten<br>Email<br>Website<br>etc</div>

    <div class="body-text" style="left:123px;top:108px">
      <div>Consequos dolupta volupti quassit haritii strunt rerestem</div>
      <div>volorio optasi que nonse ad que et voluptas debis pariasin nit,</div>
      <div>cusam, que volest quia si doloria comnis arcilluptaes etur? Qui</div>
      <div>imminciatur?</div>
    </div>
    <div class="body-text" style="left:137px;top:169px">
      <div>Consequos dolupta volupti quassit haritii strunt rerestem</div>
      <div>volorio optasi que nonse ad que et voluptas debis pariasin</div>
      <div>nit, cusam, que volest quia si doloria comnis arcilluptaes</div>
      <div>etur? Qui imminciatur?</div>
    </div>
    <div class="body-text" style="left:123px;top:230px">
      <div>Peribus aliquamust pla nobis nobitio nemquia cum fugia cus</div>
      <div>aut quaeriae. Oluptae nima pa porectat.</div>
      <div>Ut laborem volupta tquatis quo ium ad et magnatiis ent.</div>
      <div>Ebis aut modis sit re occatis as imintiaepta simpore, sit aut</div>
      <div>illorecto con esto beritiusaes etur?</div>
    </div>
    <div class="body-text" style="left:123px;top:302px">
      <div style="padding-left:14px">Peribus aliquamust pla nobis nobitio nemquia cum fugia</div>
      <div style="padding-left:14px">cus aut quaeriae. Oluptae nima pa porectat.</div>
      <div style="padding-left:14px">Ut laborem volupta tquatis quo ium ad et magnatiis ent.</div>
      <div style="padding-left:40px">Ebis aut modis sit re occatis as imintiaepta simpore,</div>
      <div style="padding-left:62px">sit aut illorecto con esto beritiusaes etur?</div>
    </div>
    <div class="body-text" style="left:123px;top:374px">
      <div style="padding-left:90px">Restor aut re, ommo berum laborepel</div>
      <div style="padding-left:101px">imi, alignim porepudae nobis ipsus au-</div>
      <div style="padding-left:110px">tem lacerum rem rerspitaes dolore</div>
      <div style="padding-left:117px">ese denimaio doles exerumquid</div>
      <div style="padding-left:124px">unditat pre voloribusdae do-</div>
      <div style="padding-left:129px">lorum assundunt et a quatibus</div>
      <div style="padding-left:133px">di si delendi storectur?</div>
    </div>
    <div class="body-text" style="left:261px;top:471px">
      <div>Restor aut re, ommo berum</div>
      <div>laborepel imi, alignim po-</div>
      <div>repudae nobis ipsus autem</div>
      <div>lacerum rem rerspitaes</div>
      <div>dolore ese denimaio doles</div>
      <div>exerumquid unditat pre volo-</div>
      <div>ribusdae dolorum assundunt</div>
    </div>

    <svg class="abs" style="left:0;top:330px" width="260" height="269" viewBox="0 0 260 269">
      <defs>
        <linearGradient id="routePhotoTone" x1="0" y1="0" x2="1" y2="1">
          <stop offset="0" stop-color="#d9d6d2"/>
          <stop offset="0.5" stop-color="#c7a797"/>
          <stop offset="1" stop-color="#e6e6e4"/>
        </linearGradient>
      </defs>
      <circle cx="118" cy="140" r="130" fill="var(--gold)"/>
      <circle cx="110" cy="146" r="126" fill="url(#routePhotoTone)" role="img" aria-label="Foto: lächelnde Frau mit Kopftuch, Warnweste und Schutzhelm"/>
    </svg>
  </section>

  <section class="page page-philosophy">
    <h2 class="heading" style="left:123px;top:33px;font-size:24px">Unsere Philosophie</h2>
    <h2 class="heading" style="left:138px;top:62px;font-size:24px">Our Philosophy</h2>

    <svg class="abs" style="left:35px;top:103px" width="70" height="70" viewBox="0 0 70 70">
      <circle cx="32" cy="37" r="32" fill="var(--gold)"/>
      <circle cx="35" cy="33" r="31" fill="#a48a72" role="img" aria-label="Foto: Mutter mit Kind"/>
    </svg>

    <div class="small-blue" style="left:37px;top:181px">„Dank der Sprach-<br>schule bin ich in<br>meinem Beruf nun<br>auf Augenhöhe mit<br>meinen Kollegen.<br>So kann ich mir<br>und meinem Kind<br>eine sichere Zu-<br>kunft schaffen.“</div>
    <div class="small-blue" style="left:37px;top:278px">„Thanks to the<br>language school<br>I am now on an<br>equal footing with<br>my colleagues in<br>my profession. That<br>way I can create a<br>secure future for<br>myself and my<br>child.“</div>
    <div class="small-blue" style="left:37px;top:383px">Leyla, Pflegekraft</div>

    <div class="body-text" style="left:123px;top:108px">
      <div>Consequos dolupta volupti quassit haritii strunt rerestem</div>
      <div>volorio optasi que nonse ad que et voluptas debis pariasin nit,</div>
      <div>cusam, que volest quia si doloria comnis arcilluptaes etur? Qui</div>
      <div>imminciatur?</div>
    </div>
    <div class="body-text" style="left:137px;top:168px">
      <div>Consequos dolupta volupti quassit haritii strunt rerestem</div>
      <div>volorio optasi que nonse ad que et voluptas debis pariasin</div>
      <div>nit, cusam, que volest quia si doloria comnis arcilluptaes</div>
      <div>etur? Qui imminciatur?</div>
    </div>
    <div class="body-text" style="left:123px;top:228px">
      <div>Peribus aliquamust pla nobis nobitio nemquia cum fugia cus</div>
      <div>aut quaeriae. Oluptae nima pa porectat.</div>
      <div>Ut laborem volupta tquatis quo ium ad et magnatiis ent.</div>
      <div>Ebis aut modis sit re occatis as imintiaepta simpore, sit aut</div>
      <div>illorecto con esto beritiusaes etur?</div>
    </div>
    <div class="body-text" style="left:137px;top:301px">
      <div>Peribus aliquamust pla nobis nobitio nemquia cum fugia</div>
      <div>cus aut quaeriae. Oluptae nima pa porectat.</div>
      <div>Ut laborem volupta tquatis quo ium ad et magnatiis ent.</div>
      <div>Ebis aut modis sit re occatis as imintiaepta simpore, sit aut</div>
      <div>illorecto con esto beritiusaes etur?</div>
    </div>
    <div class="body-text" style="left:123px;top:374px">
      <div>Restor aut re, ommo berum laborepel imi, alignim porepudae</div>
      <div>nobis ipsus autem lacerum rem rerspitaes dolore ese denimaio</div>
      <div>doles exerumquid unditat pre voloribusdae dolorum assund-</div>
      <div>unt et a quatibus di si delendi storectur?</div>
    </div>
    <div class="body-text" style="left:137px;top:434px">
      <div>Restor aut re, ommo berum laborepel imi, alignim pore-</div>
      <div>pudae nobis ipsus autem lacerum rem rerspitaes dolore</div>
      <div>ese denimaio doles exerumquid unditat pre voloribusdae</div>
      <div>dolorum assundunt et a quatibus di si delendi storectur?</div>
    </div>

    <svg class="abs" style="left:0;top:540px" width="60" height="59" viewBox="0 0 60 59">
      <circle cx="27" cy="61" r="31" fill="var(--gold)"/>
    </svg>
    <span class="page-number">1</span>
  </section>

  <section class="page page-services">
    <h2 class="heading" style="left:88px;top:34px;font-size:24px">Unsere Angebot</h2>
    <h2 class="heading" style="left:115px;top:63px;font-size:24px">Our Services</h2>

    <svg class="abs" style="left:320px;top:103px" width="70" height="70" viewBox="0 0 70 70">
      <circle cx="32" cy="37" r="32" fill="var(--gold)"/>
      <circle cx="35" cy="33" r="31" fill="#9a6e5c" role="img" aria-label="Foto: junger Mann mit älterer Frau"/>
    </svg>

    <div class="small-blue" style="left:322px;top:181px">„Ich wollte immer<br>einen Beruf haben,<br>in dem ich für an-<br>dere da sein kann.<br>Jetzt habe ich die<br>Möglichkeit dazu.“</div>
    <div class="small-blue" style="left:322px;top:248px">„I always wanted a<br>job where I could<br>be there for others.<br>Now I have the<br>opportunity.“</div>
    <div class="small-blue" style="left:322px;top:306px">Darius, Pflegekraft</div>

    <div class="offer-list" style="left:55px;top:108px">
      <div class="offer-item" style="left:0;top:0"><span class="dot dot-gold"></span>A1, A2, B1. B2, C1<br>Fachsprache Ärzte<br>Fachsprache Pflegepersonal<br>Fachsprache Ingenieure</div>
      <div class="offer-item" style="left:17px;top:55px"><span class="dot dot-royal"></span>A1, A2, B1. B2, C1<br>Doctors’ jargon<br>Technical language nursing staff<br>Technical language engineers</div>
      <div class="offer-item" style="left:0;top:123px"><span class="dot dot-gold"></span>Businessplan für Migranten<br>Unternehmensführung für Migranten<br>Ausbildung zur Pflegefachkraft<br>Existenzgründung für Migranten</div>
      <div class="offer-item" style="left:17px;top:181px"><span class="dot dot-royal"></span>Business plan for migrants<br>Corporate governance for migrants<br>Training as a nursing specialist<br>Business start-up for migrants</div>
      <div class="offer-item" style="left:0;top:253px"><span class="dot dot-gold"></span>El expedit dolupta qui aut pa de<br>tur ad eaturio nsequatur,<br>apiet inciis qui nat.</div>
      <div class="offer-item" style="left:17px;top:295px"><span class="dot dot-royal"></span>El expedit dolupta<br>qui aut pa de<br>tur ad eaturio<br>nsequatur,<br>apiet inciis<br>qui nat.</div>
    </div>

    <svg class="abs" style="left:125px;top:350px" width="299" height="249" viewBox="0 0 299 249">
      <defs>
        <linearGradient id="servicesPhotoTone" x1="0" y1="0" x2="1" y2="1">
          <stop offset="0" stop-color="#9fae9a"/>
          <stop offset="0.5" stop-color="#3e4a52"/>
          <stop offset="1" stop-color="#c9cfd3"/>
        </linearGradient>
      </defs>
      <circle cx="181" cy="189" r="180" fill="var(--gold)"/>
      <circle cx="189" cy="193" r="176" fill="url(#servicesPhotoTone)" role="img" aria-label="Foto: Gruppe junger Erwachsener im Gespräch am Besprechungstisch"/>
    </svg>
  </section>

</div>
</body>
</html>
```